Seed Company Looking For a Soybean Seed Bag Design

We are are a regional seed company who is currently launching a new line of soybean products. The brand of the product will be Tru-Crop. We are looking for a custom design of a soybean bag measuring 16"x5"x30" (when constructed). We are looking for a modern design that's relatively loud, but not too busy. The proof needs to match with the attached template. We have also provided a proof of a previous bag project (Fox-Ridge-Standard) we've done to show how the artwork needs to be laid out. In no way does the new design need to resemble the example. Also attached are some other examples of seed bags.
Industry/Entity Type
Agriculture
Colors
Designer to choose colors to be used in the design.
Look and feel
Each slider illustrates characteristics of the customer's brand and the style your logo design should communicate.

```html
<!DOCTYPE html>
<html lang="en">
<head>
<meta charset="utf-8">
<title>Tru-Crop Soy Bean Bag Design</title>
<link rel="stylesheet" href="https://fonts.googleapis.com/css2?family=Montserrat:ital,wght@0,500;0,700;1,300&family=Oswald:wght@300;600&display=swap">
<style>
  :root {
    --ink: #111111;
    --green: #2e9e48;
    --green-deep: #33964a;
    --yellow: #fbb81c;
    --sun: #f4b21e;
    --field-gold: #e9b359;
    --field-light: #f3cf83;
    --hill-green: #5a6b4b;
    --bag-light: #f3f3f3;
    --bag-dark: #e1e1e1;
    --paper: #ffffff;
    --grey-text: #666666;
  }
  * { box-sizing: border-box; margin: 0; padding: 0; }
  html, body { width: 1200px; height: 1200px; overflow: hidden; background: var(--paper); }
  .board { position: relative; width: 1200px; height: 1200px; font-family: "Montserrat", sans-serif; color: var(--ink); }

  .board-title {
    position: absolute; left: 124px; top: 42px;
    font-weight: 300; font-style: italic; font-size: 47px; letter-spacing: 2px; white-space: nowrap;
  }
  .board-label { position: absolute; font-weight: 300; font-style: italic; font-size: 50px; letter-spacing: 2px; }
  .label-mockup { left: 120px; top: 322px; }
  .label-layout { left: 689px; top: 403px; }

  .sky { position: absolute; left: 0; right: 0;
    background: linear-gradient(to bottom, rgba(255,255,255,0) 0%, rgba(179,182,230,0.55) 60%, rgba(255,255,255,0) 100%); }
  .sun { position: absolute; border-radius: 50%; background: var(--sun); }
  .fields { position: absolute; left: 0; right: 0; bottom: 0;
    background: linear-gradient(to bottom, var(--field-light) 0%, var(--field-gold) 55%, var(--hill-green) 82%, var(--hill-green) 100%); }
  .brand { position: absolute; left: 0; right: 0; text-align: center; }
  .brand-name { display: block; font-family: "Montserrat", sans-serif; font-weight: 700; color: var(--green); }
  .brand-tag { display: block; font-weight: 500; color: var(--grey-text); white-space: nowrap; text-transform: uppercase; }
  .product-box { position: absolute; background: var(--green-deep); text-align: center; color: #fff; font-family: "Oswald", sans-serif; }
  .product-box .line-bold { display: block; font-weight: 600; }
  .product-box .line-light { display: block; font-weight: 300; }
  .beans { position: absolute; left: 6%; right: 6%; background: #e8c36e; border-radius: 14px; }

  .bag-front { position: absolute; left: 65px; top: 412px; width: 348px; height: 728px; overflow: hidden;
    background: linear-gradient(to bottom, var(--bag-light), var(--bag-dark)); }
  .bag-front .sky { top: 40px; height: 90px; }
  .bag-front .sun { left: 221px; top: 24px; width: 50px; height: 50px; }
  .bag-front .brand { top: 205px; }
  .bag-front .brand-name { font-size: 28px; }
  .bag-front .brand-tag { font-size: 7px; margin-top: 8px; }
  .bag-front .product-box { left: 22px; top: 364px; width: 298px; height: 227px; border-radius: 22px; padding-top: 32px; }
  .bag-front .line-bold { font-size: 68px; line-height: 66px; }
  .bag-front .line-light { font-size: 68px; line-height: 70px; }
  .bag-front .beans { top: 184px; height: 36px; }
  .bag-front .fields { height: 112px; }

  .layout { position: absolute; left: 483px; top: 486px; width: 681px; height: 524px; border: 1px solid #222; overflow: hidden; background: var(--paper); }
  .panel { position: absolute; top: 0; height: 100%; }
  .gusset { width: 93px; background: var(--yellow); }
  .gusset-1 { left: 0; }
  .gusset-2 { left: 391px; }
  .gusset-band { position: absolute; left: 0; top: 53px; width: 100%; height: 419px; background: var(--green);
    display: flex; justify-content: center; align-items: flex-start; padding-top: 26px; }
  .gusset-text { writing-mode: vertical-rl; font-family: "Oswald", sans-serif; color: #fff; font-size: 60px; line-height: 93px; white-space: nowrap; }
  .gusset-text b { font-weight: 600; }
  .gusset-text span { font-weight: 300; }
  .front { left: 93px; width: 298px; }
  .back { left: 484px; width: 197px; }
  .layout .sky { top: 38px; height: 58px; }
  .front .sun { left: 191px; top: 7px; width: 44px; height: 44px; }
  .back .sun { left: 91px; top: 1px; width: 44px; height: 44px; }
  .layout .fields { height: 80px; }
  .front .brand { top: 122px; }
  .front .brand-name { font-size: 18px; }
  .front .brand-tag { font-size: 5px; margin-top: 5px; }
  .front .product-box { left: 43px; top: 265px; width: 211px; height: 168px; border-radius: 16px; padding-top: 24px; }
  .front .line-bold { font-size: 52px; line-height: 52px; }
  .front .line-light { font-size: 52px; line-height: 50px; }
  .front .beans { top: 136px; height: 26px; }
</style>
</head>
<body>
<main class="board">
  <h1 class="board-title">TRU-CROP SOY BEAN BAG DESIGN</h1>
  <p class="board-label label-mockup">Mockup</p>
  <p class="board-label label-layout">Full Layout</p>

  <section class="bag-front">
    <div class="sky" role="img" aria-label="Soft clouds drifting across the sky"></div>
    <div class="sun"></div>
    <div class="brand">
      <span class="brand-name">TRU-CROP</span>
      <span class="brand-tag">Grown for every season ahead</span>
    </div>
    <div class="product-box">
      <span class="line-bold">SOY BEAN</span>
      <span class="line-light">SEED</span>
      <div class="beans" role="img" aria-label="Row of golden soybeans"></div>
    </div>
    <div class="fields" role="img" aria-label="Rolling golden fields with dark trees on a green hill"></div>
  </section>

  <section class="layout">
    <div class="panel gusset gusset-1">
      <div class="gusset-band"><p class="gusset-text"><b>SOY BEAN</b> <span>SEED</span></p></div>
    </div>
    <div class="panel front">
      <div class="sky" role="img" aria-label="Soft clouds drifting across the sky"></div>
      <div class="sun"></div>
      <div class="brand">
        <span class="brand-name">TRU-CROP</span>
        <span class="brand-tag">Grown for every season ahead</span>
      </div>
      <div class="product-box">
        <span class="line-bold">SOY BEAN</span>
        <span class="line-light">SEED</span>
        <div class="beans" role="img" aria-label="Row of golden soybeans"></div>
      </div>
      <div class="fields" role="img" aria-label="Rolling golden fields with dark trees on a green hill"></div>
    </div>
    <div class="panel gusset gusset-2">
      <div class="gusset-band"><p class="gusset-text"><b>SOY BEAN</b> <span>SEED</span></p></div>
    </div>
    <div class="panel back">
      <div class="sky" role="img" aria-label="Soft clouds drifting across the sky"></div>
      <div class="sun"></div>
      <div class="fields" role="img" aria-label="Rolling golden fields with dark trees on a green hill"></div>
    </div>
  </section>
</main>
</body>
</html>
```